someone who can choose good colours and fonts and a style for an already layed out web page

HI

We need someone who can choose good colors and fonts and style for an already layed out web page.

please look at the first file.

The hard part of what needs to go where is already done,

1) we just need a type of character suitable for our business

2) colors probably in the green / yellow spectrum to suit our business

3) we need you to choose the style. For example you could choose round photos, or square buttons, video boxes with or without frames, that sort of stuff, just tweaking of what is there. plain arial is probably what we'd like but with text but with script or memorable headings. We would just like a design style that you think would be good gor our business model.

4) the twitter,facebook logo needs to be put in a new place

our project is an Italian style village in Italy called "Casale Delle Ginestre", in Abruzzo, Italy.
It is surrounded by vineyards, lake and olive trees.

The most important is that it looks expensive, the village is eco friendly so anything on those lines is great, Obviously Italian, so italian looking characters

our website is www.collinaserena.example but we are updating it. we like the style of the old site , but it is too out of date

you can create the layout using the files we've given below and boxes
Updates

hi we've just updated out brief to make it more simple, its actually not much work its just about design choices

Target Market(s)

all lovers of Italian things
eco frienly

Industry/Entity Type

Business

Font styles to use
Decorative
Script

Colors
fcf9ce
faee3f
fde18a
fece3e
cadf82
9bcb3b
acd036
fce7d2
ec2027

Requirements
Must have
• has to have the same layout or similar so as all the boxes and links are in there
twitter,facebook and other logos need to be present where you want them
Nice to have
• we have chosen some colors but you can choose others 3 or 4 are usual a good number with a light yellow background maybe....
Should not have
• no old style must look up to date

```html
<!DOCTYPE html>
<html lang="en">
<head>
<meta charset="utf-8">
<title>Casale Delle Ginestre</title>
<link rel="stylesheet" href="https://fonts.googleapis.com/css2?family=Kaushan+Script&family=Parisienne&family=Satisfy&display=swap">
<style>
  :root{
    --cream:#fcf9ce;
    --band:#f7f3b4;
    --green:#9bcb3b;
    --green-light:#cadf82;
    --green-dark:#2e4a12;
    --ink:#111;
    --footer:#585858;
    --white:#fff;
  }
  *{box-sizing:border-box;margin:0;padding:0}
  html,body{width:1069px;height:1200px;overflow:hidden;background:var(--cream)}
  body{position:relative;font-family:"Kaushan Script",cursive;color:var(--ink)}
  .abs{position:absolute}

  .site-header{left:0;top:0;width:1069px;height:100px;background:var(--cream);box-shadow:0 3px 4px rgba(0,0,0,.25)}
  .brand-mark{left:40px;top:14px;width:70px;height:70px;border-radius:50%;background:var(--green-dark)}
  .brand-name{left:138px;top:6px;font-family:"Parisienne",cursive;font-size:64px;color:var(--green-dark);white-space:nowrap}
  .newsletter{left:725px;top:0;width:344px;height:100px;background:var(--green-light);clip-path:polygon(95px 0,100% 0,100% 100%,0 100%);
    display:flex;align-items:center;justify-content:flex-end;padding-right:14px;font-size:23px;color:var(--green-dark)}

  .main-nav{left:0;top:113px;width:1069px;height:59px}
  .nav-tab{position:absolute;top:0;height:59px;display:flex;align-items:center;justify-content:center;font-size:25px;color:var(--white);
    background:linear-gradient(#a5d445,#86b82c);clip-path:polygon(34px 0,100% 0,calc(100% - 34px) 100%,0 100%);text-shadow:0 1px 2px rgba(0,0,0,.3)}
  .nav-tab.current{background:linear-gradient(#d8ea9a,#9bcb3b);color:var(--ink);text-shadow:none;clip-path:polygon(0 0,100% 0,calc(100% - 34px) 100%,0 100%)}

  .site-plan{left:0;top:192px;width:603px;height:372px;background:linear-gradient(135deg,#fbf6d6,#b9d774 55%,#8cc04a);border:1px solid #cfcaa0;box-shadow:1px 2px 4px rgba(0,0,0,.3)}
  .gallery{left:612px;top:192px;width:449px;height:296px;background:linear-gradient(#b7d3ea 0%,#e4eef2 28%,#8aa05a 45%,#6d7f3a 75%,#a59a5f 100%);border:1px solid #bbb}
  .gallery-arrow{top:120px;width:52px;height:52px;background:rgba(155,203,59,.75)}
  .gallery-dots{right:10px;bottom:8px;display:flex;gap:8px}
  .gallery-dots span{width:20px;height:20px;border-radius:50%;background:rgba(155,203,59,.6)}
  .gallery-dots span:first-child{background:#b8dc53;box-shadow:0 0 0 2px rgba(255,255,255,.5)}

  .season-row{left:612px;top:503px;height:40px;display:flex;align-items:center;gap:3px}
  .season-label{font-size:19px;margin-right:4px}
  .season-btn{width:85px;height:40px;border:1px solid #c9c6a6;background:var(--cream);box-shadow:1px 1px 3px rgba(0,0,0,.2);
    display:flex;align-items:center;justify-content:center;font-size:16px}
  .season-rule{left:612px;top:558px;width:449px;height:1px;background:linear-gradient(90deg,transparent,#aaa,transparent)}

  .intro{left:0;top:585px;width:1069px;height:231px;background:var(--band);padding:7px 20px 0 56px;font-size:16.4px;line-height:24px}
  .intro p{white-space:nowrap}

  .book-trip{left:820px;top:820px;width:232px;height:63px;background:var(--green-light);box-shadow:1px 2px 4px rgba(0,0,0,.3);
    display:flex;align-items:center;justify-content:center;font-family:"Satisfy",cursive;font-size:38px}
  .blog-card{top:883px;width:202px;height:178px;box-shadow:1px 2px 4px rgba(0,0,0,.35);display:flex;align-items:center;justify-content:center;
    font-size:24px;color:#eaf3c2;text-shadow:0 0 6px #000}
  .blog-old{left:13px;background:linear-gradient(160deg,#e7c75a,#7a5a1c 50%,#3a3a12)}
  .blog-new{left:266px;background:linear-gradient(#f0b96a,#5a7ea0 45%,#2d4a66 70%,#3d2c22)}
  .blog-divider{left:238px;top:905px;width:1px;height:134px;background:#999}
  .video{left:707px;top:890px;width:351px;height:176px;background:linear-gradient(#243045,#3e5a38 60%,#2a3a22)}
  .video-play{left:144px;top:69px;width:64px;height:38px;border-radius:8px;background:#111}

  .site-footer{left:0;top:1073px;width:1069px;height:127px;background:var(--footer)}
  .follow{left:8px;top:17px;font-size:17px;color:#ccc}
  .social{left:12px;top:49px;display:flex;gap:6px}
  .social span{width:27px;height:27px;border-radius:50%;background:#3b6fb5}
  .social span:nth-child(2){background:#4ea6d8}
  .social span:nth-child(3){background:#c9352a}
  .legal{left:240px;top:22px;width:540px;font-family:Arial,sans-serif;color:#111;font-size:19px;line-height:24px}
  .legal strong{display:block;font-size:19px}
  .contact{left:826px;font-size:19px;color:#eee;display:flex;align-items:center;gap:14px}
</style>
</head>
<body>

<header class="site-header abs">
  <div class="brand-mark abs"></div>
  <div class="brand-name abs">Casale Delle Ginestre</div>
</header>
<div class="newsletter abs">Sign Up for Newsletter</div>

<nav class="main-nav abs">
  <div class="nav-tab current" style="left:0;width:256px">Description</div>
  <div class="nav-tab" style="left:252px;width:270px">Which reason?</div>
  <div class="nav-tab" style="left:504px;width:284px">Price list</div>
  <div class="nav-tab" style="left:740px;width:329px;clip-path:polygon(34px 0,100% 0,100% 100%,0 100%)">Contact us</div>
</nav>

<div class="site-plan abs" role="img" aria-label="Illustrated site plan of the village phases, lake, park and plots"></div>

<div class="gallery abs" role="img" aria-label="Photo of the countryside with olive groves, a pond and hills">
  <svg class="gallery-arrow abs" style="left:0" viewBox="0 0 52 52"><path d="M32 12 L18 26 L32 40" stroke="#4a5a2a" stroke-width="6" fill="none"/></svg>
  <svg class="gallery-arrow abs" style="right:0" viewBox="0 0 52 52"><path d="M20 12 L34 26 L20 40" stroke="#4a5a2a" stroke-width="6" fill="none"/></svg>
  <div class="gallery-dots abs"><span></span><span></span><span></span></div>
</div>

<div class="season-row abs">
  <span class="season-label">more photos:</span>
  <span class="season-btn">Summer</span>
  <span class="season-btn">Autumn</span>
  <span class="season-btn">Winter</span>
  <span class="season-btn">Spring</span>
</div>
<div class="season-rule abs"></div>

<section class="intro abs">
  <p>Casale delle Ginestre is built in traditional Italian architectural style and surrounded by olive groves, vineyards,</p>
  <p>a beautiful lake surrounded by a park with wildlife. The panoramic view of the mountains is breathtaking and you</p>
  <p>can see for 30 miles on a clear day. Red and white umbrellas, barbeques, swimming pools and a spa will contribute to</p>
  <p>its unique atmosphere. there will also be a health farm, where you can treat yourself to a luxurious massage.</p>
  <p>Ten shops and ensure any of your other needs can be met. Casale delle Ginestre is ensconced in the beauty of the Italian</p>
  <p>countryside, where the hot white sandy beaches of the Adriatic coastline meet the cold snowy ski-slopes of the</p>
  <p>Appenine mountains, with Rome only a short car ride away.</p>
  <p>Each property will be in the OLD Abruzzo style, with attractive brick and stone walls. There are one-, two- and three-</p>
  <p>bedroomed apartments and three- or four-bedroomed villas.</p>
</section>

<div class="book-trip abs">Book Trip</div>

<div class="blog-card blog-old abs" role="img" aria-label="Photo of an autumn forest">Old blog</div>
<div class="blog-divider abs"></div>
<div class="blog-card blog-new abs" role="img" aria-label="Photo of a sea pier at sunset">New blog</div>

<div class="video abs" role="img" aria-label="Video still of a house beside a garden pond at dusk">
  <svg class="video-play abs" viewBox="0 0 64 38"><rect width="64" height="38" rx="8" fill="#111"/><path d="M26 10 L42 19 L26 28 Z" fill="#fff"/></svg>
</div>

<footer class="site-footer abs">
  <div class="follow abs">Follow us on:</div>
  <div class="social abs" aria-label="Social links"><span></span><span></span><span></span></div>
  <div class="legal abs">
    <strong>(c) 2013 Casale Delle Ginestre - CasaColle Italia S.r.l.</strong>
    More properties for sale in Abruzzo, Italy CasaColle Italia
  </div>
  <div class="contact abs" style="top:14px">
    <svg width="22" height="18" viewBox="0 0 22 18"><path d="M2 6 Q11 -1 20 6 L17 9 L14 7 L14 5 Q11 4 8 5 L8 7 L5 9 Z M5 10 L17 10 L19 17 L3 17 Z" fill="#111"/></svg>
    <span>0851234567</span>
  </div>
  <div class="contact abs" style="top:46px;font-size:17px">
    <svg width="22" height="20" viewBox="0 0 22 20"><path d="M1 10 L11 2 L21 10 M4 8 L4 19 L18 19 L18 8" stroke="#111" stroke-width="2" fill="none"/><rect x="9" y="12" width="4" height="7" fill="#111"/></svg>
    <span>Via dei Pini 12 Colleverde</span>
  </div>
</footer>

</body>
</html>
```